Hot-air ballooning company needs a DL-size flyer

Skylark Aerial Tours is a hot-air ballooning company which flies passengers in the King Valley, Victoria, Australia.
We need a 2-sided DL-size flyer which promotes our hot-air balloon flights and packages.
Most of our customers are couples, and we want the flyer design to communicate safety, adventure, and romance.
The flyer should make the best use of our images which we provide, and we've also included a document with the text for the flyer.
Updates

2 days is not long enough to gather designs, the brief never asked me what my deadline should be.

Target Market(s)

Couples, buyers are majority female, between the ages of 20-60

Industry/Entity Type

Tourism

Font styles to use
Sans Serif

Colors

Designer to choose colors to be used in the design.

Requirements
Must have
• Communicate safety, adventure, and romance
• Use images
Nice to have
• There is a lot of text, it would be great if you could make it look like as little text as possible
Should not have
• No childish designs

```html
<!DOCTYPE html>
<html lang="en">
<head>
<meta charset="utf-8">
<title>Skylark Aerial Tours – DL Flyer</title>
<link href="https://fonts.googleapis.com/css2?family=Oswald:wght@500;700&family=Montserrat:wght@400;600&display=swap" rel="stylesheet">
<style>
  :root{
    --sky:#1ea0dc;
    --sky-deep:#1a8fc8;
    --ink:#1d1d1f;
    --white:#ffffff;
    --mist:#eef0f2;
    --bg:#d9d9d9;
    --text:#222;
  }
  *{margin:0;padding:0;box-sizing:border-box}
  html,body{width:1200px;height:1200px;overflow:hidden;background:var(--bg)}
  body{position:relative;font-family:'Montserrat',sans-serif;color:var(--text)}
  .flyer{position:absolute;top:39px;width:547px;height:1125px;overflow:hidden;background:var(--white);box-shadow:0 4px 14px rgba(0,0,0,.25)}
  .flyer--front{left:33px}
  .flyer--back{left:614px;background:var(--mist)}
  .flyer svg.shapes{position:absolute;inset:0}
  .abs{position:absolute}

  /* front */
  .brand{left:318px;top:84px;width:222px;white-space:nowrap;font-weight:600;font-size:18px;color:var(--sky-deep);display:flex;align-items:center;gap:8px;justify-content:center}
  .brand .dot{width:12px;height:12px;border-radius:50%;background:var(--sky-deep);flex:none}
  .title{left:24px;top:436px;color:var(--white);font-family:'Oswald',sans-serif}
  .title h1{font-size:58px;font-weight:700;line-height:1;letter-spacing:.5px}
  .title h2{font-size:27px;font-weight:700;line-height:1.1;margin-top:2px}
  .title p{font-family:'Montserrat',sans-serif;font-size:21px;line-height:26px;margin-top:12px;width:200px}
  .intro{left:26px;top:666px;white-space:nowrap;font-size:17.4px;line-height:25.8px;color:var(--text)}

  /* back */
  .headline{left:0;top:319px;width:547px;text-align:center;font-family:'Oswald',sans-serif;font-weight:700;font-size:28px;line-height:31px;color:var(--sky-deep)}
  .lead{left:0;top:400px;width:547px;text-align:center;white-space:nowrap;font-size:17.2px;line-height:25.6px;color:var(--text)}
  .tag{left:36px;top:496px;width:210px;height:60px}
  .tag span{position:absolute;left:34px;top:12px;font-family:'Oswald',sans-serif;font-weight:500;font-size:28px;letter-spacing:1px;color:var(--sky)}
  .features{left:50px;top:580px;width:470px;list-style:none;font-weight:600;font-size:14.6px;line-height:24px;color:var(--ink);white-space:nowrap}
  .features li{position:relative;padding-left:24px}
  .features li.gap{margin-bottom:7px}
  .features li::before{content:"";position:absolute;left:0;top:7px;width:9px;height:9px;border-right:3px solid var(--sky);border-bottom:3px solid var(--sky);transform:rotate(-45deg)}
  .cta{left:125px;top:954px;width:302px;height:26px;border-radius:13px;background:var(--ink);color:var(--sky);text-align:center;font-family:'Oswald',sans-serif;font-weight:500;font-size:17px;line-height:26px}
  .contact{left:0;top:966px;width:547px;height:88px;background:var(--sky);color:var(--white);font-weight:600;font-size:14px}
  .contact .web{position:absolute;left:48px;top:18px;line-height:18px}
  .contact .call{position:absolute;left:346px;top:18px;line-height:17px}
  .contact .social{position:absolute;left:40px;top:60px;display:flex;align-items:center;gap:6px;font-size:13.4px}
  .contact .social i{display:inline-block;width:17px;height:17px;border-radius:50%;background:var(--ink)}
  .licence{left:0;top:1064px;width:547px;text-align:center;color:var(--sky);font-weight:600;font-size:13.5px;line-height:16px}
</style>
</head>
<body>

<section class="flyer flyer--front">
  <svg class="shapes" width="547" height="1125" viewBox="0 0 547 1125">
    <defs>
      <linearGradient id="dawnSky" x1="0" y1="0" x2="0" y2="1">
        <stop offset="0" stop-color="#3d8fd0"/><stop offset=".6" stop-color="#a9c4dc"/><stop offset="1" stop-color="#6b5a46"/>
      </linearGradient>
      <linearGradient id="valley" x1="0" y1="0" x2="0" y2="1">
        <stop offset="0" stop-color="#4f98d4"/><stop offset=".4" stop-color="#b9cde0"/><stop offset="1" stop-color="#5d5640"/>
      </linearGradient>
      <linearGradient id="burner" x1="0" y1="0" x2="0" y2="1">
        <stop offset="0" stop-color="#f39a2c"/><stop offset=".5" stop-color="#e5c040"/><stop offset="1" stop-color="#3a3a48"/>
      </linearGradient>
      <linearGradient id="morning" x1="0" y1="0" x2="0" y2="1">
        <stop offset="0" stop-color="#2e7cc8"/><stop offset=".6" stop-color="#bcd3e6"/><stop offset="1" stop-color="#8c8a7c"/>
      </linearGradient>
    </defs>
    <!-- top photo -->
    <rect role="img" aria-label="Photo: colourful hot-air balloons over a misty winery estate at dawn" width="547" height="419" fill="url(#dawnSky)"/>
    <polygon points="231,0 547,0 547,177 337,177" fill="var(--sky)"/>
    <polygon points="243,0 547,0 547,167 342,167" fill="var(--white)"/>

    <!-- collage -->
    <polygon role="img" aria-label="Photo: balloons drifting over fog-filled vineyards" points="430,419 547,419 547,1125 268,1125 268,600" fill="url(#valley)"/>
    <polygon points="423,419 432,419 268,590 268,600 258,600" fill="var(--white)"/>
    <polygon points="0,419 423,419 195,653 0,653" fill="var(--sky)"/>
    <polygon points="195,653 258,600 268,600 268,653" fill="var(--white)"/>
    <rect x="0" y="653" width="268" height="436" fill="var(--white)"/>
    <polygon role="img" aria-label="Photo: balloon being inflated with burner flame at dawn" points="240,893 368,805 464,953 344,1025" fill="url(#burner)" stroke="var(--white)" stroke-width="7"/>
    <polygon role="img" aria-label="Photo: balloons over a misty valley at sunrise" points="331,1033 463,953 547,1065 547,1125 383,1125" fill="url(#morning)" stroke="var(--white)" stroke-width="7"/>
    <polygon points="269,637 365,801 277,849" fill="var(--ink)"/>
    <polygon points="287,985 367,1125 191,1125" fill="var(--ink)"/>
    <polygon points="0,1089 211,1089 191,1125 0,1125" fill="var(--sky)"/>
    <polygon points="547,1070 547,1125 500,1125" fill="var(--white)"/>
  </svg>
  <div class="abs brand"><span class="dot"></span>Skylark Aerial Tours</div>
  <div class="abs title">
    <h1>KING VALLEY</h1>
    <h2>HOT-AIR BALLOONING</h2>
    <p>The perfect gourmet ballooning experience</p>
  </div>
  <p class="abs intro">Live the romance and<br>adventure of flying the<br>beautiful King Valley<br>and surrounds ina<br>hot-air balloon at dawn<br>From the vineyards and<br>patchwork of fields the<br>views expand to the<br>Ovens River,<br>spectacular Mt Buffalo<br>and the High Country<br>beyond The mountain<br>views, once aloft, come<br>to life in dramatic 3D<br>with the early<br>morning light</p>
</section>

<section class="flyer flyer--back">
  <svg class="shapes" width="547" height="1125" viewBox="0 0 547 1125">
    <defs>
      <linearGradient id="river" x1="0" y1="0" x2="1" y2="1">
        <stop offset="0" stop-color="#c89a4a"/><stop offset=".5" stop-color="#8a6a48"/><stop offset="1" stop-color="#5f8a3c"/>
      </linearGradient>
    </defs>
    <rect role="img" aria-label="Photo: passengers in a balloon basket above a river and autumn trees" width="547" height="292" fill="url(#river)"/>
    <rect x="0" y="290" width="547" height="80" fill="var(--sky)"/>
    <path d="M0,325 Q273,261 547,325 V370 H0 Z" fill="var(--ink)"/>
    <path d="M0,357 Q273,245 547,357 V1125 H0 Z" fill="var(--mist)"/>
    <rect x="0" y="1054" width="547" height="71" fill="var(--ink)"/>
  </svg>
  <h2 class="abs headline">Celebrate your flight<br>with a delicious breakfast afterwards</h2>
  <p class="abs lead">Milawa is conveniently located less than an hour's<br>drive from most places in Victoria's North East and<br>Albury in NSW Mansfield flights are also available</p>
  <div class="abs tag">
    <svg width="210" height="60" viewBox="0 0 210 60"><polygon points="22,0 210,0 188,60 0,60" fill="var(--sky)"/><polygon points="22,6 198,6 180,60 4,60" fill="var(--ink)"/></svg>
    <span>Yourflight</span>
  </div>
  <ul class="abs features">
    <li>One-hour sunrise balloon flight in the spectacular King<br>Valley region in North East Victoria</li>
    <li>Delicious champagne breakfast after the flight<br>(recommended option)</li>
    <li>Informative details throughout your experience with our<br>locally based expert crew</li>
    <li class="gap">The opportunity to be involved in the inflation and<br>deflation process should you wish</li>
    <li>Safe, friendly and professional</li>
    <li>The flight lasts approximately 1 hour</li>
    <li>The entire experience takes about 3-4 hours</li>
    <li>Suitable from age 7 to 97</li>
    <li>Gift Vouchers are also available</li>
    <li>Contact us for exclusive flight options at<br>your custom location</li>
  </ul>
  <div class="abs contact">
    <div class="web">www.skylarkaerialtours.com.au<br>flights@skylarkaerialtours.com.au</div>
    <div class="call">call our friendly team<br>on 1300 482 719</div>
    <div class="social">Find us also on <i></i><i></i><i></i> Reviews@skylarkaerialtoursaustralia</div>
  </div>
  <div class="abs cta">For bookings or more information</div>
  <p class="abs licence">Skylark Aerial Tours operates under<br>Air Operator’s Certificate C482310-05</p>
</section>

</body>
</html>
```